political advertisement for magazine

9.135 in 12.125 in. My wife is running for Judge. She needs an ad for an African-American Magazine ASAP . The ad is about a testimonial by one of her clients that makes her relatable to the African-American community. I am uploading the text for the testimonial, the picture of my wife and her client, her logo, a possible backdrop and also a slogan.

This is going in a church publication geared toward the African American Community

• The image of all the people in the back. On top of that image, you have "The people stand behind Lorena for Circuit Court Judge". Also you have a letter from her client with a picture of both of them. Also include the vote for Lorena logo and her headshot. The above is just my idea if you have an idea that is totally different but portrays that Lorena is for the people, I am ok with that too. thanks!

```html
<!DOCTYPE html>
<html lang="en">
<head>
<meta charset="utf-8">
<title>Lorena for Circuit Court Judge</title>
<link rel="stylesheet" href="https://fonts.googleapis.com/css2?family=Jost:wght@400;600&family=Playfair+Display+SC:wght@700&display=swap">
<style>
  :root {
    --red: #e8282b;
    --navy: #1f3b70;
    --ink: #111111;
    --white: #ffffff;
    --crowd-light: #f3f3f3;
    --crowd-mid: #e2e2e2;
    --portrait-warm: #8a6a55;
    --portrait-dark: #2a2523;
  }
  * { margin: 0; padding: 0; box-sizing: border-box; }
  html, body { width: 904px; height: 1200px; overflow: hidden; background: var(--white); }
  .ad {
    position: relative;
    width: 904px;
    height: 1200px;
    border: 11px solid var(--red);
    overflow: hidden;
    font-family: "Jost", "Futura", sans-serif;
    color: var(--ink);
  }
  .crowd-backdrop {
    position: absolute;
    inset: 0;
    background: linear-gradient(160deg, var(--crowd-light) 0%, var(--crowd-mid) 50%, var(--crowd-light) 100%);
  }
  .headline {
    position: absolute;
    left: 68px;
    top: 58px;
    width: 760px;
    font-family: "Playfair Display SC", "Georgia", serif;
    font-weight: 700;
    font-size: 39px;
    line-height: 46px;
    color: var(--red);
  }
  .letter {
    position: absolute;
    left: 68px;
    top: 176px;
    width: 747px;
    font-size: 24px;
    line-height: 33px;
  }
  .letter p { text-align: justify; margin-bottom: 16px; }
  .letter .closing { margin-top: 30px; text-align: left; }
  .letter .signer { font-weight: 600; display: block; }
  .client-photo-frame {
    position: absolute;
    left: 496px;
    top: 505px;
    width: 319px;
    height: 330px;
    background: var(--white);
    padding: 11px;
    box-shadow: 0 8px 8px rgba(0,0,0,0.3);
  }
  .client-photo {
    width: 100%;
    height: 100%;
    background: linear-gradient(180deg, #4d6a3a 0%, #7c9a5e 40%, #c3d3e3 70%, #e4e8ee 100%);
  }
  .vote-band {
    position: absolute;
    left: 0;
    right: 0;
    bottom: 0;
    height: 309px;
    background: var(--navy);
  }
  .headshot {
    position: absolute;
    left: 0;
    bottom: 0;
    width: 461px;
    height: 565px;
    background: linear-gradient(180deg, var(--portrait-warm) 0%, var(--portrait-dark) 100%);
  }
  .campaign-name {
    position: absolute;
    left: 506px;
    top: 930px;
    width: 310px;
    text-align: center;
    font-weight: 600;
    font-size: 30px;
    line-height: 40px;
    text-transform: uppercase;
    letter-spacing: 1px;
    color: var(--white);
  }
  .disclaimer {
    position: absolute;
    left: 506px;
    top: 1111px;
    width: 310px;
    text-align: center;
    font-size: 12.5px;
    line-height: 18.5px;
    color: var(--white);
  }
</style>
</head>
<body>
<div class="ad">
  <div class="crowd-backdrop" role="img" aria-label="Faded grid of smiling faces from the community"></div>

  <h1 class="headline">The people stand behind Lorena<br>for Circuit Court Judge</h1>

  <div class="letter">
    <p>For the past few years, Lorena Castell Moreno has been my lawyer. She has always strived to provide excellence in legal services. Her almost encyclopedic knowledge of the law makes for a flawless, precise, navigation of the legal system, with results.</p>
    <p>She is the epitome of professionalism, that is aptly balanced by her calm persona. Her empathy is more than commendable, and her legal experience unmatched.</p>
    <p>Lorena Castell Moreno is truly one of kind, deserving of all accolades, appointments, and accomplishments.</p>
    <p class="closing">Yours Truly,<span class="signer">Darnell Whitaker</span></p>
  </div>

  <div class="client-photo-frame">
    <div class="client-photo" role="img" aria-label="Photo of Lorena shaking hands with her client in front of a flowering hedge"></div>
  </div>

  <div class="vote-band"></div>
  <div class="headshot" role="img" aria-label="Portrait headshot of Lorena in a black blazer and pearl necklace"></div>

  <p class="campaign-name">Vote Lorena<br>Castell Moreno<br>for Judge</p>

  <p class="disclaimer">Political Advertisement paid for and approved by<br>the Committee to Elect Lorena Castell Moreno,<br>no party affiliation, for Circuit Court Judge</p>
</div>
</body>
</html>
```